Calibrated NET Systems
Business card and Stationary
Project: Calibrated NET Systems
Calibrated NET Systems - Information Technology
Creative Brief
Professional
Dean Harlowe
Technical Consultant
Please leave the address part blank.
dean.harlowe@calnet.ca
www.calnet.ca

```html
<!DOCTYPE html>
<html lang="en">
<head>
<meta charset="utf-8">
<title>Calibrated NET Systems – Stationery</title>
<link href="https://fonts.googleapis.com/css2?family=Questrial&display=swap" rel="stylesheet">
<style>
  :root{
    --bg:#8a8c90;
    --paper:#ffffff;
    --blue-deep:#0b4f86;
    --blue:#1f7fc0;
    --blue-light:#6cc2ee;
    --grey-line:#c9ced3;
    --grey-flap:#9ea5ad;
    --ink:#3d4a57;
    --ink-soft:#7a8591;
  }
  *{box-sizing:border-box;margin:0;padding:0}
  html,body{width:1200px;height:665px;overflow:hidden}
  body{background:var(--bg);font-family:"Questrial",sans-serif;color:var(--ink);position:relative}
  .piece{position:absolute;background:var(--paper);box-shadow:0 2px 6px rgba(0,0,0,.18);overflow:hidden}
  .band{position:absolute;background:linear-gradient(90deg,var(--blue-deep),var(--blue) 60%,var(--blue-light))}
  .brand{position:absolute;display:flex;align-items:center;gap:6px;white-space:nowrap}
  .brand-mark{background:var(--blue);flex:none}
  .brand-name{color:var(--blue);line-height:1;font-weight:400}
  .brand.on-blue .brand-mark{background:var(--paper)}
  .brand.on-blue .brand-name{color:var(--paper)}

  /* business card */
  .card{left:46px;top:292px;width:250px;height:146px}
  .card .band{left:0;top:0;width:132px;height:146px}
  .card .brand{left:12px;top:58px}
  .card .brand-mark{width:10px;height:10px}
  .card .brand-name{font-size:8.5px}
  .card-person{position:absolute;right:12px;top:14px;text-align:right}
  .card-person .name{font-size:11px;color:var(--ink)}
  .card-person .title{font-size:7px;color:var(--blue);margin-top:2px}
  .card-contact{position:absolute;right:12px;top:60px;text-align:right;font-size:6px;line-height:1.7;color:var(--ink-soft)}
  .partner-badge{position:absolute;left:12px;bottom:16px;width:34px;height:10px;background:var(--paper);opacity:.85}

  /* letterhead */
  .letterhead{left:330px;top:86px;width:334px;height:472px}
  .letterhead .band{left:0;bottom:0;width:334px;height:64px}
  .letterhead .brand{left:26px;top:38px}
  .letterhead .brand-mark{width:14px;height:14px}
  .letterhead .brand-name{font-size:13px}
  .letterhead-contact{position:absolute;right:24px;top:32px;font-size:6px;line-height:1.8;color:var(--ink-soft);border-left:1px solid var(--grey-line);padding-left:6px}

  /* envelope back */
  .envelope-back{left:716px;top:70px;width:440px;height:204px}
  .envelope-back .brand{left:168px;top:96px}
  .envelope-back .brand-mark{width:10px;height:10px}
  .envelope-back .brand-name{font-size:9px}

  /* envelope front */
  .envelope-front{left:716px;top:318px;width:440px;height:206px}
  .envelope-front .band-top{left:0;top:0;width:440px;height:62px}
  .envelope-front .band-bottom{left:0;bottom:0;width:440px;height:34px}
  .envelope-front .brand{left:22px;top:23px}
  .envelope-front .brand-mark{width:14px;height:14px}
  .envelope-front .brand-name{font-size:14px}
</style>
</head>
<body>

<section class="piece card" aria-label="Business card">
  <div class="band" role="img" aria-label="Blue gradient band artwork"></div>
  <div class="brand on-blue"><span class="brand-mark"></span><span class="brand-name">Calibrated NET Systems</span></div>
  <div class="card-person"><div class="name">Dean Harlowe</div><div class="title">Technical Consultant</div></div>
  <div class="card-contact">
    <div>T 416 555 0142</div>
    <div>M 416 555 0187</div>
    <div>dean.harlowe@calnet.ca</div>
    <div>www.calnet.ca</div>
    <div>S dharlowe</div>
  </div>
  <span class="partner-badge"></span>
</section>

<section class="piece letterhead" aria-label="Letterhead">
  <div class="band" role="img" aria-label="Blue gradient band artwork"></div>
  <div class="brand"><span class="brand-mark"></span><span class="brand-name">Calibrated NET Systems</span></div>
  <div class="letterhead-contact">
    <div>T 416 555 0142</div>
    <div>F 416 555 0143</div>
    <div>dean.harlowe@calnet.ca</div>
    <div>www.calnet.ca</div>
  </div>
</section>

<section class="piece envelope-back" aria-label="Envelope back">
  <svg width="440" height="204" viewBox="0 0 440 204" style="position:absolute;left:0;top:0">
    <rect x="0" y="0" width="440" height="34" fill="var(--grey-flap)"/>
    <path d="M0 34L200 130L440 34" fill="none" stroke="#d6dade" stroke-width="1.5"/>
    <path d="M0 204L190 120M440 204L230 122" fill="none" stroke="#e2e5e8" stroke-width="1.2"/>
  </svg>
  <div class="brand"><span class="brand-mark"></span><span class="brand-name">Calibrated NET Systems</span></div>
</section>

<section class="piece envelope-front" aria-label="Envelope front">
  <div class="band band-top" role="img" aria-label="Blue gradient band artwork"></div>
  <div class="band band-bottom" role="img" aria-label="Blue gradient band artwork"></div>
  <div class="brand on-blue"><span class="brand-mark"></span><span class="brand-name">Calibrated NET Systems</span></div>
</section>

</body>
</html>
```